Flyer-Design für Datenschutzorganisation
Zielgruppe
Unsere Zielgruppe sind mittelständische Unternehmen ohne Ärzte und Apotheken, Mitarbeiterzahl 1-100 Personen, wir unterstützen Unternehmer und Unternehmen bei der Umsetzung der EU-Datenschutzgrundverordnung im Betrieb, wir sind ein VORTA-zertifiziertes Beratungsunternehmen
Aufgabenstellung
'Unsere vornehmliche Aufgabe liegt im Aufbau und der Umsetzung einer praxisnahen und gesetzeskonformen Datenschutzorganisation in Ihrem Unternehmen.'
'Nur wer alle Regeln kennt, kann sie auch einhalten'
'Egal, ob aus Ressourcengründen oder um den Blick eines externen Experten zu erhalten – unsere Beratung macht Sinn. Im Mittelpunkt steht dabei immer Ihr Unternehmen, Ihre Mitarbeiter und Ihre Projekte.'
'Wir sorgen für eine datenschutzkonforme Ausgestaltung der Prozesse in Ihrem Unternehmen im Umgang mit personenbezogenen Daten, ausgerichtet an der Zielsetzung Ihres Geschäftsmodells. Sie erhalten somit ein Rundum-sorglos-Paket im Datenschutz.'

```html
<!DOCTYPE html>
<html lang="de">
<head>
<meta charset="utf-8">
<title>Flyer Datenschutzorganisation</title>
<link rel="stylesheet" href="https://fonts.googleapis.com/css2?family=Roboto:wght@400;700;900&display=swap">
<style>
  :root {
    --brown: #5e3d21;
    --white: #ffffff;
    --ink: #111111;
    --paper: #ffffff;
    --grey-light: #ecebea;
    --grey-mid: #d9d8d6;
    --photo-light: #dfe3e6;
    --photo-dark: #6e625a;
  }
  * { margin: 0; padding: 0; box-sizing: border-box; }
  html, body {
    width: 848px; height: 1200px; overflow: hidden;
    background: var(--paper);
    font-family: "Roboto", Arial, sans-serif;
  }
  .sheet { position: relative; width: 848px; height: 1200px; }
  .format-note {
    position: absolute; left: 52px; top: 54px;
    font-size: 18px; font-weight: 400; color: var(--ink);
  }
  .flyer {
    position: absolute; left: 215px; top: 215px;
    width: 430px; height: 861px;
    box-shadow: 0 0 4px rgba(0,0,0,0.18);
    overflow: hidden;
  }
  .headline-band {
    position: absolute; left: 0; top: 0; width: 430px; height: 516px;
    background: var(--brown);
  }
  .headline {
    position: absolute; left: 17px; top: 18px;
    color: var(--white);
    font-weight: 700; font-size: 63px; line-height: 61px;
    letter-spacing: -2px; text-transform: uppercase;
  }
  .arrow-down { position: absolute; left: 41px; top: 454px; }
  .contact-row {
    position: absolute; left: 0; top: 516px; width: 430px; height: 173px;
    background: var(--white);
  }
  .brand {
    position: absolute; left: 16px; top: 40px;
    display: flex; align-items: center; gap: 8px;
    color: var(--brown); font-weight: 700; font-size: 26px; letter-spacing: 0.5px;
  }
  .brand-square { width: 22px; height: 22px; background: var(--brown); }
  .company {
    position: absolute; left: 16px; top: 121px;
    color: var(--brown); font-size: 15px; line-height: 17px;
  }
  .company .web { font-weight: 700; }
  .photo-meeting {
    position: absolute; left: 215px; top: 0; width: 215px; height: 173px;
    background: linear-gradient(120deg, var(--photo-light) 0%, #c9c4bd 45%, var(--photo-dark) 100%);
  }
  .photo-dsgvo {
    position: absolute; left: 0; top: 689px; width: 430px; height: 172px;
    background: linear-gradient(180deg, var(--grey-light) 0%, var(--grey-mid) 100%);
  }
</style>
</head>
<body>
<div class="sheet">
  <p class="format-note">Format: 105 mm x 210 mm</p>

  <section class="flyer">
    <div class="headline-band">
      <h1 class="headline">„Nur<br>wer alle<br>Regeln<br>kennt,<br>kann sie<br>auch<br>einhalten.“</h1>
      <svg class="arrow-down" width="82" height="42" viewBox="0 0 82 42" aria-hidden="true">
        <polygon points="0,0 82,0 41,42" fill="#ffffff"/>
      </svg>
    </div>

    <div class="contact-row">
      <div class="brand"><span class="brand-square"></span>LINDMOOR</div>
      <p class="company">Lindmoor Consulting GmbH<br><span class="web">www.lin-con.de</span></p>
      <div class="photo-meeting" role="img" aria-label="Foto: zwei Berater besprechen einen Vertrag am Schreibtisch"></div>
    </div>

    <div class="photo-dsgvo" role="img" aria-label="Bild: weiße 3D-Buchstaben mit Paragrafenzeichen und DSGVO"></div>
  </section>
</div>
</body>
</html>
```